New, clean letterhead for law firm in Colorado using recently designed logo.

Professional letterhead for established law firm rebranding. We service high end clientele with mostly family law and personal injury cases. Need source files for future changes. Prefer logo at top, names of members and staff in left margin, contact info in footer.

Target Market(s)

High wealth individuals

Contact Information for Business Card

Need options for traditional and square two sided business cards

Font styles to use
Serif

Colors
0555a3

Requirements
Must have
• Our logo; blue, gray, and white; modern feel.
Should not have
• Images of people

```html
<!DOCTYPE html>
<html lang="en">
<head>
<meta charset="utf-8">
<title>Alderwood Hale Law, LLC — Business Card</title>
<link rel="stylesheet" href="https://fonts.googleapis.com/css2?family=Arimo:wght@400;700&display=swap">
<style>
  :root {
    --stage: #5b5b5b;
    --card-black: #151515;
    --card-black-soft: #1d1d1d;
    --silver: #b8b8b8;
    --silver-dim: #8e8e8e;
    --edge-blue: #2c6ec6;
  }
  * { margin: 0; padding: 0; box-sizing: border-box; }
  html, body { width: 1200px; height: 1200px; overflow: hidden; }
  body {
    background: var(--stage);
    position: relative;
    font-family: "Arimo", Arial, sans-serif;
  }
  .card {
    position: absolute;
    left: 160px;
    width: 880px;
    height: 503px;
    background: linear-gradient(160deg, var(--card-black-soft), var(--card-black) 60%);
    border-bottom: 10px solid var(--edge-blue);
    box-shadow: 0 10px 30px rgba(0,0,0,.35);
    overflow: hidden;
  }
  .card--back { top: 70px; }
  .card--front { top: 627px; }

  /* Back side */
  .holder {
    position: absolute;
    right: 500px;
    top: 196px;
    text-align: right;
    color: var(--silver-dim);
  }
  .holder__name { font-size: 27px; font-weight: 700; letter-spacing: .3px; }
  .holder__title { font-size: 17px; margin-top: 2px; }
  .divider {
    position: absolute;
    left: 402px;
    top: 180px;
    width: 1px;
    height: 96px;
    background: var(--silver-dim);
  }
  .contact-list {
    position: absolute;
    left: 424px;
    top: 184px;
    list-style: none;
    color: var(--silver-dim);
    font-size: 15px;
    line-height: 30px;
  }
  .contact-list li { display: flex; align-items: center; gap: 10px; }
  .contact-list svg { width: 16px; height: 16px; flex: none; }
  .address {
    position: absolute;
    left: 300px;
    bottom: 52px;
    color: var(--silver-dim);
    font-size: 15px;
    letter-spacing: .2px;
  }

  /* Front side */
  .brand {
    position: absolute;
    left: 0; right: 0;
    top: 150px;
    display: flex;
    flex-direction: column;
    align-items: center;
    gap: 34px;
  }
  .brand__mark {
    width: 110px;
    height: 110px;
    border-radius: 50%;
    background: #6f6f6f;
  }
  .brand__name {
    font-family: "Arimo", Arial, sans-serif;
    font-weight: 400;
    color: var(--silver);
    font-size: 40px;
    letter-spacing: 2px;
    text-transform: uppercase;
    white-space: nowrap;
  }
</style>
</head>
<body>
  <section class="card card--back" aria-label="Card back">
    <div class="holder">
      <p class="holder__name">Daniel Reyes</p>
      <p class="holder__title">President</p>
    </div>
    <div class="divider"></div>
    <ul class="contact-list">
      <li>
        <svg viewBox="0 0 16 16" fill="none" stroke="currentColor" stroke-width="1.4"><path d="M4 1.8l2.2 3-1.3 1.6c.8 1.8 2 3 3.8 3.8l1.6-1.3 3 2.2-1 2.3C7.5 14.2 1.8 8.5 1.7 2.8z"/></svg>
        +00 000 000 000
      </li>
      <li>
        <svg viewBox="0 0 16 16" fill="none" stroke="currentColor" stroke-width="1.4"><rect x="1.5" y="3.5" width="13" height="9"/><path d="M1.5 3.5L8 9l6.5-5.5"/></svg>
        info@alderwoodhale.com
      </li>
      <li>
        <svg viewBox="0 0 16 16" fill="none" stroke="currentColor" stroke-width="1.3"><circle cx="8" cy="8" r="6.5"/><ellipse cx="8" cy="8" rx="2.8" ry="6.5"/><path d="M1.5 8h13"/></svg>
        www.alderwoodhale.com
      </li>
    </ul>
    <p class="address">0000 Street Ave. unit 000 New York, CA 00000</p>
  </section>

  <section class="card card--front" aria-label="Card front">
    <div class="brand">
      <div class="brand__mark" role="img" aria-label="Firm logo placeholder"></div>
      <h1 class="brand__name">Alderwood Hale Law, LLC</h1>
    </div>
  </section>
</body>
</html>
```